WBP Business Cards

I need business cards for "willow bend partners llc" doublesided... logo on the back (also include logo on front)
logo attached to project... i have jpg up.. let me know if you need eps file.
Company Info:
742 East Harlow Avenue, Suite 8D
Chicago, Illinois 60417
facsimile 312-481-2267 (list fax, address, website on all cards.)
www.willowbendpartnersllc.example
Three different people on cards:
Darius K. Whitcomb, CPA MST
Principal
ofc 312-481-3900
mobile 312-574-8816
dariuskwhitcomb@willowbendpartnersllc.example
Peter J. Olundsen, CPA MST
Principal
peterjolundsen@willowbendpartnersllc.example
mobile 708-613-4471
ofc 312-481-3900
Alvin M Crandby
Principal
ofc 312-481-3900
no mobile
alvinmcrandby@willowbendpartnersllc.example
I have multiple projects listed.. see below:
Business cards for willow bend partners llc
letterhead
envelopes
Business cards for KT Holdings LLC
letterhead
envelopes
Target Market(s)
rich people
Industry/Entity Type
Business
Look and feel

```html
<!DOCTYPE html>
<html lang="en">
<head>
<meta charset="utf-8">
<title>Willow Bend Partners LLC – Business Cards</title>
<link href="https://fonts.googleapis.com/css2?family=Tinos:ital,wght@0,400;0,700;1,400&family=Arimo:wght@700&display=swap" rel="stylesheet">
<style>
  :root {
    --navy: #17314f;
    --brand-blue: #1d4577;
    --band-light: #2f5f99;
    --ink: #1b2b44;
    --paper: #ffffff;
    --edge: #3a3a3a;
  }
  * { margin: 0; padding: 0; box-sizing: border-box; }
  html, body { width: 1200px; height: 927px; overflow: hidden; background: var(--paper); }
  body { position: relative; font-family: "Tinos", "Times New Roman", serif; color: var(--ink); }

  .side-label {
    position: absolute; top: 62px; width: 200px; text-align: center;
    font-family: "Arimo", Arial, sans-serif; font-weight: 700; font-size: 24px; color: #111;
  }
  .side-label--front { left: 190px; }
  .side-label--back { left: 740px; }

  .card {
    position: absolute; width: 528px; height: 303px; overflow: hidden;
    background: var(--paper); border: 1px solid var(--edge);
    box-shadow: 0 14px 18px -10px rgba(0,0,0,0.18);
  }
  .card--classic-front { left: 52px; top: 132px; }
  .card--classic-back { left: 604px; top: 132px; }
  .card--wave-front { left: 52px; top: 540px; }
  .card--wave-back { left: 606px; top: 537px; }

  .wordmark {
    position: absolute; color: var(--brand-blue); font-weight: 400;
    text-transform: uppercase; white-space: nowrap; text-align: center;
  }
  .wordmark--small { font-size: 12px; letter-spacing: 0.6px; }
  .wordmark--large { font-size: 24px; letter-spacing: 1px; left: 0; width: 528px; }

  .contact-panel {
    position: absolute; left: 237px; top: 0; width: 291px; height: 100%;
    background: var(--navy); color: #fff; padding: 48px 0 0 34px;
  }
  .person-name { font-weight: 700; font-size: 19px; line-height: 1; }
  .person-title { font-style: italic; font-size: 13px; margin-top: 8px; }
  .contact-lines { font-size: 14px; line-height: 17px; margin-top: 14px; }
  .contact-lines b { font-weight: 700; display: inline-block; width: 38px; }
  .contact-email { font-size: 11px; }
  .contact-web { font-size: 14px; margin-top: 17px; }

  .wave { position: absolute; left: 0; bottom: 0; width: 528px; height: 303px; }

  .wave-front-name {
    position: absolute; right: 32px; top: 80px; text-align: right;
    color: var(--ink); font-weight: 700; font-size: 19px; line-height: 1;
  }
  .wave-front-title {
    position: absolute; right: 32px; top: 106px; font-style: italic; font-size: 13px;
  }
  .wave-front-address {
    position: absolute; left: 18px; top: 151px; font-size: 13.5px; line-height: 18px;
  }
  .wave-front-phones {
    position: absolute; left: 376px; top: 151px; font-size: 13.5px; line-height: 25px;
  }
  .wave-front-phones b { display: inline-block; width: 42px; font-weight: 700; }
  .wave-front-email {
    position: absolute; right: 30px; top: 208px; font-size: 11.5px;
  }
  .wave-front-web {
    position: absolute; left: 0; width: 528px; top: 282px; text-align: center;
    color: #fff; font-size: 13.5px;
  }
</style>
</head>
<body>
  <div class="side-label side-label--front">FRONT</div>
  <div class="side-label side-label--back">BACK</div>

  <!-- Classic front -->
  <section class="card card--classic-front">
    <div class="wordmark wordmark--small" style="left:0; width:237px; top:172px;">Willow Bend Partners llc</div>
    <div class="contact-panel">
      <div class="person-name">Alvin M. Crandby</div>
      <div class="person-title">CPA MST Principal</div>
      <div class="contact-lines">
        742 East Harlow Avenue, Suite 8D<br>
        Chicago, Illinois 60417<br>
        <b>Tel.</b>312.481.3900<br>
        <b>Fax.</b>312.481.2267<br>
        <span class="contact-email">alvinmcrandby@willowbendpartnersllc.example</span>
      </div>
      <div class="contact-web">www.willowbendpartnersllc.example</div>
    </div>
  </section>

  <!-- Classic back -->
  <section class="card card--classic-back">
    <div class="wordmark wordmark--large" style="top:134px;">Willow Bend Partners llc</div>
  </section>

  <!-- Wave front -->
  <section class="card card--wave-front">
    <div class="wordmark wordmark--small" style="left:0; width:240px; top:80px;">Willow Bend Partners llc</div>
    <div class="wave-front-name">Alvin M. Crandby</div>
    <div class="wave-front-title">CPA MST Principal</div>
    <div class="wave-front-address">742 East Harlow Avenue, Suite 8D<br>Chicago, Illinois 60417</div>
    <div class="wave-front-phones">
      <b>Tel.</b>312.481.3900<br>
      <b>Fax.</b>312.481.2267
    </div>
    <div class="wave-front-email">alvinmcrandby@willowbendpartnersllc.example</div>
    <svg class="wave" viewBox="0 0 528 303" aria-hidden="true">
      <path d="M0,200 Q250,300 528,258 L528,303 L0,303 Z" fill="var(--band-light)"/>
      <path d="M0,212 Q250,312 528,268 L528,303 L0,303 Z" fill="var(--navy)"/>
    </svg>
    <div class="wave-front-web">www.willowbendpartnersllc.example</div>
  </section>

  <!-- Wave back -->
  <section class="card card--wave-back">
    <div class="wordmark wordmark--large" style="top:180px;">Willow Bend Partners llc</div>
    <svg class="wave" viewBox="0 0 528 303" aria-hidden="true">
      <path d="M0,255 Q300,275 528,205 L528,303 L0,303 Z" fill="var(--band-light)"/>
      <path d="M0,266 Q300,285 528,218 L528,303 L0,303 Z" fill="var(--navy)"/>
    </svg>
  </section>
</body>
</html>
```